Personal sales brochure for client marketing

I am looking for a brochure in the style of a sales menu to sit in front of clients with. I want 5 different colored columns where clients will choose the right package for them.
Eg.
Package 1 called Book-keeping is a basic package
Package 2 called Insight includes the above but also extra services
Package 3 called Compliance an add on for the above packages
Package 4 Called Professional another add on to the above services
Package 5 called payroll another add on to the above.

I want to sit in front of my clients and discuss the services we provide and allow them to choose from this list and tick the boxes of what they would like. I attach a simple spread sheet as well for guideline.

Target Market(s)

business owners requiring accounting support and advice

Industry/Entity Type

Accounting

Font styles to use
Serif
Sans Serif

Requirements
Must have
• Simple, clear, concise with clear product descriptions in colored boxes that highlight clearly the different options. Must have Logo and contact details. This document need to be our key sales and marketing tool so will need to introduce the business clearly and in a professional manner.
• enquiries@brantwellpartners.gg
• 01481 439216
Nice to have
• The design needs to be printable on A1 A3 A4 A5
Should not have
• Pictures and patterns

```html
<!DOCTYPE html>
<html lang="en">
<head>
<meta charset="utf-8">
<title>Brantwell &amp; Partners – Packages</title>
<link href="https://fonts.googleapis.com/css2?family=Roboto+Condensed:wght@400;700&family=Roboto:wght@400;700&family=Raleway:wght@500&display=swap" rel="stylesheet">
<style>
  :root{
    --bg:#e9e9e9;
    --paper:#ffffff;
    --ink:#3c3c3e;
    --brand-grey:#58585a;
    --soft-green:#b7d9b3;
    --payroll:#2ea84a;   --payroll-tab:#1b5c2e;
    --books:#57585a;     --books-tab:#2a2a2b;
    --insight:#4275b9;   --insight-tab:#13274a;
    --comply:#13ab97;    --comply-tab:#0d4a44;
    --pro:#f26a22;       --pro-tab:#5a2a12;
    --night:#16161a;
    --line:#6a6a6a;
  }
  *{box-sizing:border-box;margin:0;padding:0}
  html,body{width:1200px;height:1200px;overflow:hidden;background:var(--bg)}
  body{position:relative;font-family:"Roboto Condensed",sans-serif;color:var(--ink)}
  .sheet{position:absolute;top:224px;width:716px;height:928px;background:var(--paper);
    transform:scale(.81);transform-origin:0 0;overflow:hidden;box-shadow:0 6px 18px rgba(0,0,0,.18)}
  .sheet--menu{left:12px}
  .sheet--order{left:608px}
  .abs{position:absolute}
  .brand-name{font-family:"Roboto Condensed",sans-serif;font-weight:400;color:var(--brand-grey);white-space:nowrap;letter-spacing:1px;font-size:40px;line-height:1}
  .brand-tag{font-family:"Raleway",sans-serif;font-weight:500;color:var(--brand-grey);letter-spacing:4.2px;white-space:nowrap;font-size:16.5px}
  .side-title{left:40px;top:196px;transform:rotate(-90deg);transform-origin:0 0;font-size:40px;color:var(--soft-green);letter-spacing:1px;white-space:nowrap;line-height:1}
  .intro{left:148px;top:146px;font-family:"Roboto",sans-serif;font-weight:700;font-size:13.4px;line-height:17px;color:var(--ink)}

  .band{position:absolute;left:0;width:716px;color:#fff}
  .band--payroll{top:207px;height:129px;background:var(--payroll)}
  .band--books{top:336px;height:129px;background:var(--books);border-top:1px solid #bbb}
  .band--insight{top:465px;height:130px;background:var(--insight);border-top:1px solid #cfd9ea}
  .band--comply{top:595px;height:125px;background:var(--comply);border-top:1px solid #cfe9e4}
  .band--pro{top:720px;height:137px;background:var(--pro)}
  .tab{position:absolute;left:0;top:0;height:31px;width:185px;clip-path:polygon(0 0,100% 0,86% 100%,0 100%);
    font-size:18.5px;line-height:31px;padding-left:28px;color:#fff}
  .band--payroll .tab{background:var(--payroll-tab);padding-left:50px}
  .band--books .tab{background:var(--books-tab)}
  .band--insight .tab{background:var(--insight-tab);padding-left:48px}
  .band--comply .tab{background:var(--comply-tab);padding-left:30px}
  .band--pro .tab{background:var(--pro-tab);padding-left:29px}
  .band-icon{position:absolute;left:48px;width:54px;height:54px}
  .list{position:absolute;left:182px;list-style:none;font-family:"Roboto",sans-serif;font-size:14.2px;line-height:21px}
  .list li::before{content:"•";margin-right:7px}
  .list .sub{font-size:11.2px;line-height:16.5px;padding-left:20px}
  .list .lead{font-family:"Roboto Condensed",sans-serif;font-weight:700;font-size:14px}
  .list .mini{font-family:"Roboto Condensed",sans-serif;font-size:12px;line-height:18px;padding-left:20px}
  .list--tight{line-height:17px}

  .foot-note{left:28px;top:870px;font-family:"Roboto Condensed",sans-serif;font-size:11px;line-height:14px;color:#444}
  .foot-band{left:426px;top:845px;width:300px;height:90px;background:var(--night);clip-path:polygon(20% 0,100% 0,100% 100%,0 100%)}
  .foot-contact{left:500px;top:854px;color:#fff;font-size:14.5px;line-height:21px;white-space:nowrap}

  .big-title{left:0;width:716px;top:158px;text-align:center;font-size:118px;line-height:1;color:var(--soft-green);font-weight:400;letter-spacing:-1px}
  .cols{position:absolute;left:0;top:260px;width:716px;height:155px;display:flex;gap:2px}
  .col{flex:1;display:flex;flex-direction:column;align-items:center;color:#fff;font-size:18.5px}
  .col svg{width:56px;height:56px;margin-top:30px}
  .col span{margin-top:22px;white-space:nowrap}
  .col--payroll{background:var(--payroll)} .col--books{background:var(--books)}
  .col--insight{background:var(--insight)} .col--comply{background:var(--comply)} .col--pro{background:var(--pro)}
  .ticks{position:absolute;top:432px;left:0;width:716px;display:flex}
  .tick-cell{flex:1;display:flex;justify-content:center}
  .box{width:36px;height:36px;border:1.5px solid #444;background:#fff}
  .box svg{display:block;width:100%;height:100%}
  .field{position:absolute;left:50px;width:610px;border-bottom:2px solid var(--line);font-size:17px;color:var(--ink);padding-left:2px;height:36px;line-height:40px}
  .small{font-family:"Roboto Condensed",sans-serif;font-size:11.5px;line-height:14px;color:#444}
  .order-foot{left:0;top:860px;width:716px;height:68px;background:var(--night);color:#fff;font-size:18px;text-align:center;line-height:52px;word-spacing:2px;white-space:nowrap}
</style>
</head>
<body>
<svg width="0" height="0" style="position:absolute" aria-hidden="true">
  <defs>
    <symbol id="i-payroll" viewBox="0 0 56 56"><g fill="none" stroke="#fff" stroke-width="2.6" stroke-linejoin="round" stroke-linecap="round">
      <path d="M30 12H10a3 3 0 0 0-3 3v32a3 3 0 0 0 3 3h32a3 3 0 0 0 3-3V28"/><path d="M44 4l7 7-20 20-9 2 2-9z"/></g></symbol>
    <symbol id="i-books" viewBox="0 0 56 56"><g fill="none" stroke="#fff" stroke-width="2.6">
      <rect x="3" y="11" width="50" height="9" rx="4"/><rect x="3" y="23" width="50" height="9" rx="4"/><rect x="3" y="35" width="50" height="9" rx="4"/></g></symbol>
    <symbol id="i-insight" viewBox="0 0 56 56"><g fill="none" stroke="#fff" stroke-width="2.6" stroke-linecap="round" stroke-linejoin="round">
      <path d="M16 18V12a3 3 0 0 1 3-3h30a3 3 0 0 1 3 3v32a3 3 0 0 1-3 3H19a3 3 0 0 1-3-3v-6"/><path d="M4 28h32M28 20l8 8-8 8"/></g></symbol>
    <symbol id="i-comply" viewBox="0 0 56 56"><g fill="none" stroke="#fff" stroke-width="2.6" stroke-linejoin="round">
      <path d="M22 4h14l10 10v26a3 3 0 0 1-3 3H22a3 3 0 0 1-3-3V7a3 3 0 0 1 3-3z"/><path d="M36 4v10h10"/>
      <path d="M19 14h-6a3 3 0 0 0-3 3v32a3 3 0 0 0 3 3h21a3 3 0 0 0 3-3v-6"/></g></symbol>
    <symbol id="i-pro" viewBox="0 0 56 56"><g fill="none" stroke="#fff" stroke-width="2.6" stroke-linejoin="round">
      <rect x="4" y="15" width="48" height="34" rx="3"/><path d="M20 15V9h16v6M4 29h48"/></g></symbol>
  </defs>
</svg>

<!-- Services menu sheet -->
<section class="sheet sheet--menu">
  <div class="abs side-title">PACKAGES</div>
  <div class="abs brand-name" style="left:150px;top:68px">BRANTWELL &amp; PARTNERS</div>
  <div class="abs brand-tag" style="left:150px;top:120px">ACCOUNTING &amp; BUSINESS SOLUTIONS</div>
  <p class="abs intro">EVERY BUSINESS IS DIFFERENT AND WHEN WE UNDERSTAND YOUR NEEDS<br>WE CAN PROVIDE JUST THE SERVICES YOU REQUIRE FOR AN AGREED FEE.<br>OUR SERVICES FALL INTO THE FOLLOWING CATEGORIES:</p>

  <div class="band band--payroll">
    <div class="tab">PAYROLL</div>
    <svg class="band-icon" style="top:48px"><use href="#i-payroll"/></svg>
    <ul class="list" style="top:12px">
      <li>Weekly/monthly</li><li>ETI Returns</li><li>UK/Channel Island</li>
    </ul>
  </div>

  <div class="band band--books">
    <div class="tab">BOOK-KEEPING</div>
    <svg class="band-icon" style="top:56px"><use href="#i-books"/></svg>
    <ul class="list" style="top:17px">
      <li>Monthly/Quarterly/Annually its your choice</li>
      <li>Invoices entered and bank accounts reconciled</li>
      <li>Purchase and sales ledgers reconciled</li>
      <li>All software is included.</li>
      <li>Unlimited support and assistance.</li>
    </ul>
  </div>

  <div class="band band--insight">
    <div class="tab">INSIGHT</div>
    <svg class="band-icon" style="top:57px"><use href="#i-insight"/></svg>
    <ul class="list list--tight" style="top:8px">
      <li>Monthly/Quarterly/Annually its your choice</li>
      <li>In addition to Book-keeping this package provides</li>
      <li class="sub">Accounting adjustments to give a true reflection of your profit/loss to date</li>
      <li class="sub">Management Accounts</li>
      <li class="sub">Regular meeting to discuss business performance and possible areas for improvement</li>
      <li>All software is included.</li>
      <li>Unlimited support and assistance.</li>
    </ul>
  </div>

  <div class="band band--comply">
    <div class="tab">COMPLIANCE</div>
    <svg class="band-icon" style="top:56px"><use href="#i-comply"/></svg>
    <ul class="list" style="top:14px">
      <li class="lead">What every business must do:</li>
      <li class="mini">Financial statements prepared</li>
      <li class="mini">Income tax computation</li>
      <li class="mini">Personal tax returns</li>
    </ul>
  </div>

  <div class="band band--pro">
    <div class="tab">PROFESSIONAL</div>
    <svg class="band-icon" style="top:61px"><use href="#i-pro"/></svg>
    <ul class="list list--tight" style="top:15px;left:185px">
      <li>Bespoke solutions for your business</li>
      <li>Business planning</li>
      <li>Cash flow planning and forecasting</li>
      <li>Specialist tax planning</li>
      <li>Business turnaround</li>
      <li>All software is included.</li>
      <li>Unlimited support and assistance.</li>
    </ul>
  </div>

  <p class="abs foot-note">Many clients have a need for a "catch-up" project to get their books and accounts up to date.<br>We will agree with you a plan to complete the project at the outset and agree a fixed price.</p>
  <div class="abs foot-band"></div>
  <div class="abs foot-contact">enquiries@brantwellpartners.gg<br>01481 439216<br>www.brantwellpartners.gg</div>
</section>

<!-- Package order sheet -->
<section class="sheet sheet--order">
  <div class="abs brand-name" style="left:0;width:716px;text-align:center;top:80px">BRANTWELL &amp; PARTNERS</div>
  <div class="abs brand-tag" style="left:0;width:716px;text-align:center;top:132px">ACCOUNTING &amp; BUSINESS SOLUTIONS</div>
  <div class="abs big-title">PACKAGES</div>

  <div class="cols">
    <div class="col col--payroll"><svg><use href="#i-payroll"/></svg><span>PAYROLL</span></div>
    <div class="col col--books"><svg><use href="#i-books"/></svg><span>BOOK-KEEPING</span></div>
    <div class="col col--insight"><svg><use href="#i-insight"/></svg><span>INSIGHT</span></div>
    <div class="col col--comply"><svg><use href="#i-comply"/></svg><span>COMPLIANCE</span></div>
    <div class="col col--pro"><svg><use href="#i-pro"/></svg><span>PROFESSIONAL</span></div>
  </div>

  <div class="ticks">
    <div class="tick-cell"><div class="box"></div></div>
    <div class="tick-cell"><div class="box"></div></div>
    <div class="tick-cell"><div class="box"><svg viewBox="0 0 36 36"><path d="M9 19l6 7 13-17" fill="none" stroke="#aaa" stroke-width="3.5" stroke-linecap="round" stroke-linejoin="round"/></svg></div></div>
    <div class="tick-cell"><div class="box"></div></div>
    <div class="tick-cell"><div class="box"></div></div>
  </div>

  <div class="field" style="top:500px">NAME</div>
  <div class="field" style="top:540px">ADDRESS</div>
  <div class="field" style="top:580px">PHONE</div>
  <div class="field" style="top:620px">COMMENT</div>
  <div class="field" style="top:658px"></div>

  <div class="abs small" style="left:562px;top:737px;font-size:12px">Signature</div>
  <p class="abs small" style="left:47px;top:765px;width:620px">"Our Fully Inclusive Packages are priced to your requirements and paid as a monthly fee based upon a 12 month contract and paid by Direct Debit. Should the contract be terminated early we reserve the right to charge for time spent to date that hasn't been invoiced."</p>
  <div class="abs" style="left:47px;top:808px;font-size:14px;line-height:21px">Rg. No. 40318<br>The Island Financial Services Commission</div>
  <div class="abs small" style="left:560px;top:836px">Terms and Conditions</div>

  <div class="abs order-foot">enquiries@brantwellpartners.gg &nbsp;&nbsp; | &nbsp;&nbsp; 01481 439216 &nbsp;&nbsp; | &nbsp;&nbsp; www.brantwellpartners.gg</div>
</section>
</body>
</html>
```